Come crowdsource a Web Design for a brazilian crowdsource Startup!

> NAME OF OUR STARTUP:
Mundaleo

> DESCRIPTION OF OUR STARTUP:
We are a crowdsourcing startup in Brazil providing consultancy and technology to support other companies to crowdsource their projects.
We also operate doing big crowdsource campaings related to polemic subjects in Brazil.

> WHAT ARE OUR TARGET AUDIENCE?
Our target audience are young people around 20-35 years old.
Generation Y (Millennial Generation)

> WHAT IS OUR INDUSTRY?
Internet, web

> WHAT DO WE NEED?
We need a Web Design for our first site.

We need 5 pages:
- Home
- What is Crowdsourcing?
- Solutions
- About Us
- Blog
- A box for the "Contact" tab (this is not a page)

Please, find attached a Layout Sketch of what I've imagined.

Lets talk about the sketch:
Well, first of all, it's a SKETCH, so you don't have to send proposals exactly as the sketch. The sketch is just to show how I've imagined the ditribution of the content boxes. For example, the menu bar doesnt need to be a rectangle exactly like the sketch, but, I would like to have the menu on the right side of the logo. Also, you will see that the boxes are all squeezed, of course I dont want them soo squeezed! Again, its juust a SKETCH!

About the images on the sketch:
IMG1 - Some nice and simple image related to collectivity or related to crowdsourcing or maybe use our O logo.

IMG2 - Some simple and creative image related to Consultancy. It doesnt need to be so obvious.

IMG3 - Some simple and creative image related to Web 2.0 Software Technology. It doesnt need to be so obvious.

IMG4 - Some simple and creative image related to a full package of Consultancy + Technology. It doesnt need to be so obvious.

IMG5 - Some nice and simple image related to collectivity or related to crowdsourcing.

IMG6 - Some nice and simple image related to Ideation. Maybe a light bulb? I dont know, be creative!

IMG7 - Some nice and simple image related to Crowdlabor. I dont know, be creative!

IMG8 - Some nice and simple image related to CrowdFeedback. Maybe a megaphone? A loudspeaker? I dont know, be creative!

IMG9 - Some nice and simple image related to us! Maybe our O logo ? I dont know, be creative!

THE CONTACT SIDE BAR - we need a nice and simple contact side bar. By the way, on the sketch this bar is shown only at the homepage, but when the site becomes real this bar will stay along all the pages.

THE CONTACT BOX - we need a nice and simple contact box.

ABOUT THE COLORS TO USE: we would like some color to our background and titles. We like colors similars to our logo: really light blue ? light green/blue ? light grey ? light orange ? I dont know, you guys knows more about that then me =)

CHATTERBOX SHARE/LIKE BUTTON: We would like a chatterbox share/like button somewhere on the site!

ABOUT THE ATTACHED FILES:

ADDITIONALS:
> The name Mundaleo comes from "collectivity". With our name we want to pass the idea of the collectivity from the crowdsource work model.

> Our communication is directed to the Generation Y.

> Remember, we are a Startup! So we need a modern and simple site, something like the web 2.0 trends. It must be beautiful =)

> We arent a serious company. We are a young and fun company! Please, dont come with old fashionable company sites.

> Be creative =] !

Target Market(s)

Our target audience are young people around 20-35 years old. Generation Y (Millennial Generation)

Industry/Entity Type

Communication

Requirements
Must have
• We need a Web Design for our first site.

We need 5 pages:
- Home
- What is Crowdsourcing?
- Solutions
- About Us
- Blog

ABOUT THE COLORS TO USE: we would like some color to our background and titles. We like colors similars to our logo: really light blue ? light green/blue ? light grey ? light oranges ? I dont know, you guys knows more about that then me =)

Should not have
• Poor/serious/old fashionable designs

```html
<!DOCTYPE html>
<html lang="en">
<head>
<meta charset="utf-8">
<title>Mundaleo – Home</title>
<link href="https://fonts.googleapis.com/css2?family=Questrial&family=Telex&family=PT+Sans:ital,wght@0,400;0,700;1,400&display=swap" rel="stylesheet">
<style>
:root{
  --teal:#1a9aa3;
  --teal-dark:#0f8a92;
  --orange:#f7941d;
  --orange-line:#e8832a;
  --ink:#1d1d1d;
  --text:#333;
  --muted:#555;
  --rule:#9a9a9a;
  --tab:#3a3a3a;
  --white:#fff;
}
*{box-sizing:border-box;margin:0;padding:0}
html,body{width:1200px;height:1135px;overflow:hidden;background:var(--white)}
body{position:relative;font-family:"PT Sans",Arial,sans-serif;color:var(--text)}
.hero{position:absolute;left:0;top:0;width:1200px;height:474px;
  background:linear-gradient(90deg,#d9ecf6 0%,#c7e2ef 35%,#b9cfe0 55%,#8fa9c6 75%,#a9c0d8 100%)}
.hero-photo{position:absolute;left:430px;top:70px;width:770px;height:404px;
  background:radial-gradient(ellipse at 50% 40%,#e6d7cc 0%,#9fb6d6 45%,#4f5f7a 80%,rgba(80,95,120,0) 100%);opacity:.75}
.site-header{position:absolute;left:0;top:0;width:1200px;height:90px;background:rgba(255,255,255,.8)}
.logo{position:absolute;left:152px;top:22px;display:flex;align-items:center;gap:10px}
.logo-dot{width:44px;height:44px;border-radius:50%;background:var(--orange)}
.logo-name{font-family:"Questrial",sans-serif;font-size:44px;color:var(--teal);line-height:1}
.main-nav{position:absolute;top:35px;left:519px;display:flex;align-items:center}
.main-nav a{font-family:"Questrial",sans-serif;font-size:14px;color:var(--ink);text-decoration:none;letter-spacing:.3px;padding:6px 10px;margin-right:9px}
.main-nav a.active{background:var(--orange);color:var(--white);border-radius:3px}
.mission{position:absolute;left:141px;top:220px;width:387px;height:174px;background:rgba(255,255,255,.55);padding:10px 16px 0 18px;overflow:hidden}
.mission h1{font-family:"Questrial",sans-serif;font-weight:400;font-size:40px;line-height:48px;color:#1e2a33;white-space:nowrap}
.mission p{font-family:"Telex",sans-serif;font-size:16px;line-height:26px;color:#1e2a33;margin-top:14px}
.contact-tab{position:absolute;left:0;top:404px;width:40px;height:139px;background:var(--tab);border-radius:0 4px 4px 0;border:1px solid #777;border-left:none;display:flex;align-items:center;justify-content:center;text-decoration:none}
.contact-tab span{transform:rotate(-90deg);color:var(--white);font-family:"Questrial",sans-serif;font-size:20px;letter-spacing:2px;white-space:nowrap}
.services{position:absolute;top:526px;left:0;width:1200px}
.service{position:absolute;width:271px;text-align:center}
.service-photo{width:271px;height:156px;border:4px solid var(--white);box-shadow:0 0 3px rgba(0,0,0,.35)}
.service h2{font-family:"Telex",sans-serif;font-weight:400;font-size:23px;line-height:30px;color:var(--teal);margin:20px -20px 0;white-space:nowrap}
.service p{font-size:13.5px;line-height:21.6px;color:var(--text);margin-top:8px;height:130px;overflow:hidden}
.service p strong{color:var(--ink)}
.btn{display:inline-block;margin-top:21px;background:var(--teal-dark);color:var(--white);font-size:11px;padding:3px 10px;text-decoration:none;line-height:15px}
.footer-line{position:absolute;left:0;top:1000px;width:1200px;height:2px;background:linear-gradient(90deg,rgba(232,131,42,.25),var(--orange-line) 20%,var(--orange-line) 80%,rgba(232,131,42,.25))}
.footer-links{position:absolute;top:1018px;left:141px;width:918px;height:40px;display:flex;font-style:italic;color:var(--muted)}
.footer-links .col{border-right:1px solid var(--rule);padding:0 22px;display:flex;flex-direction:column;justify-content:center;font-size:17px;white-space:nowrap}
.footer-links .col:first-child{padding-left:0}
.footer-links .phones{font-size:12px;color:var(--orange);font-style:italic}
.newsletter{padding-left:24px;font-size:16px;white-space:nowrap}
.newsletter .field{margin-top:4px;width:216px;height:18px;background:#e3e3e3;border:1px solid #ccc;position:relative}
.newsletter .go{position:absolute;right:2px;top:2px;width:13px;height:12px;background:var(--orange)}
.orange-band{position:absolute;left:0;top:1074px;width:1200px;height:6px;background:var(--orange-line)}
.copyright{position:absolute;left:141px;top:1096px;font-size:12px;color:#333}
.like{position:absolute;right:141px;top:1093px;display:flex;align-items:center;gap:6px;font-size:10px;color:#333}
.like-btn{border:1px solid #9aa;background:#eef0f5;padding:2px 5px;font-size:10px;color:#3b5076}
.like-sq{width:11px;height:11px;background:#3b5998}
</style>
</head>
<body>
<div class="hero" role="img" aria-label="Team of five smiling young professionals standing with arms crossed in a bright office">
  <div class="hero-photo"></div>
</div>
<header class="site-header">
  <div class="logo"><span class="logo-dot"></span><span class="logo-name">Mundaleo</span></div>
  <nav class="main-nav">
    <a class="active" href="#">HOME</a>
    <a href="#">WHAT IS CROWDSOURCING?</a>
    <a href="#">SOLUTIONS</a>
    <a href="#">ABOUT US</a>
    <a href="#">BLOG</a>
  </nav>
</header>
<section class="mission">
  <h1>Mundaleo Mission:</h1>
  <p>Here we tell our mission in a few lines. Lorem ipsum dolor sit amet, consectetur adipiscing elit. Vestibulum lectus ante, lacininon, pelelit.</p>
</section>
<a class="contact-tab" href="#"><span>CONTACT</span></a>
<section class="services">
  <article class="service" style="left:142px">
    <div class="service-photo" role="img" aria-label="Three colleagues reviewing documents together at a table" style="background:linear-gradient(135deg,#dfe6ec,#9bb3c9 50%,#5d6f80)"></div>
    <h2>Consultancy</h2>
    <p><strong>Here we have a short description of our Consultancy service.</strong> Lorem ipsum dolor sit amet, consectetur adipiscing elit. Vestibulum lectus ante, lacinia eu ultrices non, pellentesque at elit. Proin malesuada pellentesque libero a consectetur. Proin</p>
    <a class="btn" href="#">Learn More</a>
  </article>
  <article class="service" style="left:476px">
    <div class="service-photo" role="img" aria-label="Hand touching a glowing screen surrounded by web icons" style="background:radial-gradient(circle at 50% 45%,#c9d0c4,#5b6455 45%,#1e241f)"></div>
    <h2>Techonlogy</h2>
    <p><strong>Here we have a short description of our Consultancy service.</strong> Lorem ipsum dolor sit amet, consectetur adipiscing elit. Vestibulum lectus ante, lacinia eu ultrices non, pellentesque at elit. Proin malesuada pellentesque libero a consectetur. Proin</p>
    <a class="btn" href="#">Learn More</a>
  </article>
  <article class="service" style="left:788px">
    <div class="service-photo" role="img" aria-label="Silver puzzle globe resting on a computer keyboard" style="background:radial-gradient(circle at 45% 50%,#9a9a9a,#d4d6d8 45%,#f0f1f2)"></div>
    <h2>Consultancy + Technology</h2>
    <p><strong>Here we have a short description of our Consultancy service.</strong> Lorem ipsum dolor sit amet, consectetur adipiscing elit. Vestibulum lectus ante, lacinia eu ultrices non, pellentesque at elit. Proin malesuada pellentesque libero a consectetur. Proin</p>
    <a class="btn" href="#">Learn More</a>
  </article>
</section>
<div class="footer-line"></div>
<footer class="footer-links">
  <div class="col" style="width:248px">Quick and Positive Response<span class="phones">+00.987.654.3210 | +00.987.654.3299</span></div>
  <div class="col">About Us</div>
  <div class="col">What is Crowdsourcing?</div>
  <div class="col">Solutions</div>
  <div class="newsletter">Subscribe Newsletter<div class="field"><span class="go"></span></div></div>
</footer>
<div class="orange-band"></div>
<p class="copyright">Copyright 2013, All rights reserved.</p>
<div class="like"><span class="like-btn">Like</span><span class="like-sq"></span><span>10 people like this.</span></div>
</body>
</html>
```